Business Card Design Project - Sports Brand

Brisk is a e-commerce fitness wear brand for ladies who are into gym, pole and swim.

Card should not be overly cluttered and should include the following:

1. logo
2. Name of the company (Use "Brisk Loom Pte Ltd" for now)
3. Address of company (Use a mock address)
4. Representative's name and contact info etc. (use a mock name and contact info)
5. website address

Target Market(s)

Women who are into pole , gym, and swim.

Women who shop online

Industry/Entity Type

E-Commerce

Colors

Designer to choose colors to be used in the design.

Requirements
Nice to have
• feminine sublimation of colours

Need not be printed on traditional paper. We would like the design to be revolutionary and interesting to the eye :)
Should not have
• the design should not be traditional looking. Do not include illustrations of Bikinis, yoga poses etc. in the card.

```html
<!DOCTYPE html>
<html lang="en">
<head>
<meta charset="utf-8">
<title>Brisk Business Card</title>
<link href="https://fonts.googleapis.com/css2?family=Open+Sans:wght@400;600&display=swap" rel="stylesheet">
<style>
  :root {
    --stage: #9a9ea3;
    --brand-red: #c42a30;
    --text-grey: #6d6a68;
    --card-silver-1: #e9e6e3;
    --card-silver-2: #cfcac6;
    --glow-yellow: #ffe9a3;
    --glow-pink: #ef9fb0;
  }
  * { margin: 0; padding: 0; box-sizing: border-box; }
  html, body { width: 1200px; height: 900px; overflow: hidden; }
  body {
    background: var(--stage);
    font-family: "Open Sans", Arial, sans-serif;
    display: flex;
    flex-direction: column;
    align-items: center;
    justify-content: center;
    gap: 56px;
  }
  .card {
    width: 580px;
    height: 340px;
    border-radius: 30px;
    position: relative;
    overflow: hidden;
    box-shadow: 0 8px 24px rgba(0,0,0,0.18);
  }
  .card-front__backdrop {
    position: absolute; inset: 0;
    background:
      radial-gradient(circle at 62% 28%, #fff8d8 0%, var(--glow-yellow) 18%, transparent 45%),
      radial-gradient(circle at 88% 20%, var(--glow-pink) 0%, transparent 40%),
      radial-gradient(circle at 12% 85%, #f9a977 0%, transparent 50%),
      linear-gradient(135deg, #f9c08f 0%, #fbd3a4 40%, #f6c6b8 70%, #eba6b8 100%);
  }
  .brand-name {
    position: absolute;
    font-family: "Open Sans", Arial, sans-serif;
    font-weight: 600;
    color: var(--brand-red);
    line-height: 1;
  }
  .card-front .brand-name { left: 0; right: 0; top: 132px; text-align: center; font-size: 66px; }

  .card-back {
    background:
      radial-gradient(circle at 70% 60%, rgba(255,255,255,0.45) 0%, transparent 35%),
      radial-gradient(circle at 20% 25%, rgba(255,255,255,0.4) 0%, transparent 40%),
      linear-gradient(160deg, var(--card-silver-1) 0%, var(--card-silver-2) 100%);
  }
  .card-back .brand-name { right: 44px; top: 40px; font-size: 40px; }

  .rep { position: absolute; left: 44px; top: 150px; }
  .rep__name { color: var(--brand-red); font-size: 26px; font-weight: 400; }
  .rep__title { color: var(--text-grey); font-size: 13px; }

  .contact {
    position: absolute; left: 44px; bottom: 36px;
    font-size: 13px; line-height: 1.55; color: var(--text-grey);
  }
  .contact__label { color: var(--brand-red); }
  .contact__web { color: var(--brand-red); }

  .company {
    position: absolute; left: 340px; top: 150px;
    font-size: 12.5px; line-height: 1.5; color: var(--text-grey);
  }
  .company__name { color: var(--brand-red); text-transform: uppercase; }
</style>
</head>
<body>
  <section class="card card-front">
    <div class="card-front__backdrop" role="img" aria-label="Soft glowing bokeh background in warm yellow, orange and pink tones"></div>
    <div class="brand-name">Brisk</div>
  </section>

  <section class="card card-back">
    <div class="brand-name">Brisk</div>

    <div class="rep">
      <div class="rep__name">Mara Lindqvist</div>
      <div class="rep__title">Your Title</div>
    </div>

    <div class="company">
      <div class="company__name">Brisk Loom Pte Ltd</div>
      <div>Level 4, 58 Harbour Lane</div>
      <div>Sydney, NSW 2000 Australia</div>
    </div>

    <div class="contact">
      <div><span class="contact__label">tel:</span> 1300 482 905 <span class="contact__label">fax:</span> 61 2 9847 3310</div>
      <div><span class="contact__label">email:</span> hello@briskloom.com</div>
      <div class="contact__web">www.briskloom.com</div>
    </div>
  </section>
</body>
</html>
```